Fennick Executive Search - New Business Card Design Project

We are an executive search firm called Fennick Executive Search based in the UK. We require a custom design for a business card. We're looking to convey a professional service to executives for executive search recruitment services. In terms of colours, we like dark blues and grays (maybe even silver incorporated somewhere if we go for a foiled type of card) but we're open to your artistic flare. See our current logo in attachments. We are totally open on design so long as the design is slick and professional.
Updates

Thanks for all your contributions of various designs. I have to say the quality of work has been amazing which is going to make our job quite difficult in the coming days on making a decision. Thanks to you all that have taken the time to submit designs thus far. We'll keep on reviewing and try to narrow down our selection as soon as possible.

Target Market(s)

Executive Search

Industry/Entity Type

Recruitment

Contact Information for Business Card

Fennick Executive Search,
Discreetly Finding & Placing Senior Executives
Gordon Pellbury, Managing Director,
07823 906417
0117 486 7132
gordon@fennickexecutive.co.uk
fennickexecutive.co.uk
58 Lindmoor Court, Hatherley Road, Harbridge, HB14 9QJ

Font styles to use
Sans Serif
Other font styles liked:
• Roboto (which is used in our logo)

Requirements
Must have
• Our logo (It has a subtle fade on it from #02071d at top to #333649 at bottom)
• The logo can be on one side or both sides
• Must be elegant and professional
• We have 2nd slogan ADVISE | ENGAGE | PLACE | SUPPORT which can be incorporated into the card
Nice to have
• Use of blues and grey colours
• Compatible with similar styling to our website fennickexecutive.co.uk
Should not have
• Must not be overly brash
• Must not contain cartoon characters

```html
<!DOCTYPE html>
<html lang="en">
<head>
<meta charset="utf-8">
<title>Fennick Executive Search – Business Card</title>
<link href="https://fonts.googleapis.com/css2?family=Roboto:wght@300;400;500;700;900&display=swap" rel="stylesheet">
<style>
  :root {
    --navy-top: #02071d;
    --navy-bottom: #333649;
    --navy: #1f2440;
    --ink: #1b1f36;
    --grey-text: #7a7c86;
    --silver-light: #f4f4f6;
    --silver-mid: #c9cacf;
    --silver-dark: #8e9098;
    --paper: #ffffff;
    --backdrop: #e7e8ec;
  }
  * { margin: 0; padding: 0; box-sizing: border-box; }
  html, body { width: 1200px; height: 900px; overflow: hidden; background: var(--backdrop); }
  body { font-family: "Roboto", Arial, sans-serif; }
  .canvas { position: relative; width: 1200px; height: 900px; overflow: hidden; background: var(--backdrop); }

  .card {
    position: absolute;
    left: 250px;
    width: 700px;
    height: 400px;
    overflow: hidden;
    box-shadow: 0 10px 26px rgba(20, 24, 45, 0.22);
  }
  .card svg.edges { position: absolute; inset: 0; width: 100%; height: 100%; }

  /* Front (navy) */
  .card-front { top: 30px; background: linear-gradient(180deg, var(--navy-top), var(--navy-bottom)); }
  .front-brand { position: absolute; left: 150px; top: 104px; color: var(--paper); }
  .front-brand .brand-name { font-weight: 700; font-size: 66px; line-height: 0.95; letter-spacing: 1px; }
  .front-brand .brand-sub { font-weight: 500; font-size: 34px; line-height: 1.1; letter-spacing: 0.5px; }
  .slogan {
    position: absolute; left: 150px; top: 268px;
    color: var(--paper); font-weight: 300; font-size: 15px; letter-spacing: 3px;
  }

  /* Back (white) */
  .card-back { top: 470px; background: var(--paper); }
  .back-brand { position: absolute; left: 40px; top: 30px; color: var(--ink); }
  .back-brand .brand-name { font-weight: 700; font-size: 56px; line-height: 0.95; letter-spacing: 1px; }
  .back-brand .brand-sub { font-weight: 500; font-size: 29px; line-height: 1.1; letter-spacing: 0.5px; }
  .back-brand .tagline { font-weight: 400; font-size: 15px; color: var(--grey-text); margin-top: 4px; }

  .contact-list { position: absolute; left: 40px; top: 176px; list-style: none; color: var(--ink); font-size: 15px; }
  .contact-list li { display: flex; align-items: center; height: 22px; }
  .contact-list svg { width: 13px; height: 13px; margin-right: 12px; fill: var(--navy); flex: none; }

  .person { position: absolute; right: 40px; top: 232px; text-align: right; color: var(--ink); }
  .person .name { font-weight: 700; font-size: 23px; color: var(--navy); }
  .person .role { font-size: 15px; margin-top: 2px; }
  .person .address { font-size: 15px; line-height: 1.35; margin-top: 16px; }
</style>
</head>
<body>
<div class="canvas">

  <section class="card card-front">
    <svg class="edges" viewBox="0 0 700 400" aria-hidden="true">
      <defs>
        <linearGradient id="silverFront" x1="0" y1="0" x2="0" y2="1">
          <stop offset="0" stop-color="var(--silver-dark)"/>
          <stop offset="0.45" stop-color="var(--silver-light)"/>
          <stop offset="1" stop-color="var(--silver-mid)"/>
        </linearGradient>
      </defs>
      <path d="M0,0 L38,0 Q8,200 38,400 L0,400 Z" fill="url(#silverFront)"/>
      <path d="M700,0 L662,0 Q692,200 662,400 L700,400 Z" fill="url(#silverFront)"/>
    </svg>
    <div class="front-brand">
      <div class="brand-name">FENNICK</div>
      <div class="brand-sub">EXECUTIVE SEARCH</div>
    </div>
    <div class="slogan">ADVISE | ENGAGE | PLACE | SUPPORT</div>
  </section>

  <section class="card card-back">
    <svg class="edges" viewBox="0 0 700 400" aria-hidden="true">
      <defs>
        <linearGradient id="silverBack" x1="0" y1="0" x2="1" y2="0">
          <stop offset="0" stop-color="var(--silver-dark)"/>
          <stop offset="0.4" stop-color="var(--silver-light)"/>
          <stop offset="1" stop-color="var(--silver-mid)"/>
        </linearGradient>
        <linearGradient id="navyBack" x1="0" y1="0" x2="0" y2="1">
          <stop offset="0" stop-color="var(--navy-bottom)"/>
          <stop offset="1" stop-color="var(--navy-top)"/>
        </linearGradient>
      </defs>
      <path d="M0,300 Q260,318 700,400 L0,400 Z" fill="url(#silverBack)"/>
      <path d="M0,318 Q280,336 700,400 L0,400 Z" fill="url(#navyBack)"/>
    </svg>

    <div class="back-brand">
      <div class="brand-name">FENNICK</div>
      <div class="brand-sub">EXECUTIVE SEARCH</div>
      <div class="tagline">Discreetly Finding &amp; Placing Senior Executives</div>
    </div>

    <ul class="contact-list">
      <li><svg viewBox="0 0 24 24"><path d="M6.6 10.8c1.4 2.8 3.8 5.1 6.6 6.6l2.2-2.2c.3-.3.7-.4 1-.2 1.1.4 2.3.6 3.6.6.6 0 1 .4 1 1V20c0 .6-.4 1-1 1C10.6 21 3 13.4 3 4c0-.6.4-1 1-1h3.5c.6 0 1 .4 1 1 0 1.3.2 2.5.6 3.6.1.3 0 .7-.2 1L6.6 10.8z"/></svg>07823 906417</li>
      <li><svg viewBox="0 0 24 24"><path d="M6 3h12v5H6zM4 9h16a2 2 0 0 1 2 2v6h-4v4H6v-4H2v-6a2 2 0 0 1 2-2zm4 7v3h8v-3z"/></svg>0117 486 7132</li>
      <li><svg viewBox="0 0 24 24"><path d="M2 5h20v14H2zm2 2v.5l8 5 8-5V7l-8 5z"/></svg>gordon@fennickexecutive.co.uk</li>
      <li><svg viewBox="0 0 24 24"><path d="M12 2a10 10 0 1 0 0 20 10 10 0 0 0 0-20zm6.9 6h-3a15 15 0 0 0-1.3-4A8 8 0 0 1 18.9 8zM12 4c.8 1.2 1.5 2.5 1.9 4h-3.8c.4-1.5 1.1-2.8 1.9-4zM4.3 14a8 8 0 0 1 0-4h3.4a16 16 0 0 0 0 4zm.8 2h3a15 15 0 0 0 1.3 4A8 8 0 0 1 5.1 16zm3-8h-3a8 8 0 0 1 4.3-4A15 15 0 0 0 8.1 8zM12 20c-.8-1.2-1.5-2.5-1.9-4h3.8c-.4 1.5-1.1 2.8-1.9 4zm2.3-6H9.7a14 14 0 0 1 0-4h4.6a14 14 0 0 1 0 4zm.3 6a15 15 0 0 0 1.3-4h3a8 8 0 0 1-4.3 4zm1.7-6a16 16 0 0 0 0-4h3.4a8 8 0 0 1 0 4z"/></svg>www.fennickexecutive.co.uk</li>
    </ul>

    <div class="person">
      <div class="name">Gordon Pellbury</div>
      <div class="role">Managing Director</div>
      <div class="address">58 Lindmoor Court, Hatherley Road<br>Harbridge, HB14 9QJ</div>
    </div>
  </section>

</div>
</body>
</html>
```